Menu sign design for Italian Deli

Need designs for 2 hanging signs - one sided, full color, full bleed.
One sign finishes at 48" wide by 36" high, the other sign finishes at 24" wide by 36" high. (Copy and Specs included in PDF).

All files to be completed in PDF format, CMYK

Fonts, layout, colors, backgrounds, photos are totally up to you. Once we see some concepts we can give you more direction/ideas.
These signs will be used in an Italian Deli....(maybe pick-up the Italian colors?????)

```html
<!DOCTYPE html>
<html lang="en">
<head>
<meta charset="utf-8">
<title>Rocco's Deli Menu Sign</title>
<link rel="stylesheet" href="https://fonts.googleapis.com/css2?family=Lobster&family=Great+Vibes&family=Archivo+Narrow:wght@700&family=Roboto:wght@400;700;900&display=swap">
<style>
  :root {
    --green: #1f8a3a;
    --green-dark: #136b2a;
    --red: #d3202a;
    --red-dark: #a3141c;
    --yellow: #ffe021;
    --white: #ffffff;
    --ink: #1a1a1a;
  }
  * { margin: 0; padding: 0; box-sizing: border-box; }
  html, body { width: 800px; height: 1200px; overflow: hidden; background: var(--white); }
  .sign { position: relative; width: 800px; height: 1200px; overflow: hidden; font-family: "Roboto", Arial, sans-serif; }
  .backdrop { position: absolute; inset: 0; }
  .block { position: absolute; left: 0; width: 100%; text-align: center; }

  .salads-title { top: 18px; font-family: "Lobster", cursive; font-size: 62px; color: var(--white); }
  .price-row { position: absolute; left: 28px; right: 40px; height: 50px; font-weight: 900; font-size: 37px; color: var(--white); }
  .price-row span { position: absolute; top: 0; }
  .price-row .label { left: 20px; }
  .price-row .label::before { content: ""; position: absolute; left: -18px; top: 18px; width: 10px; height: 10px; border-radius: 50%; background: var(--yellow); }
  .price-row .small { left: 230px; }
  .price-row .large { left: 500px; }
  .price-row b { color: var(--yellow); font-weight: 900; }
  .row-plain { top: 128px; }
  .row-specialty { top: 194px; }
  .row-divider { position: absolute; left: 20px; top: 183px; width: 700px; height: 2px; background: rgba(255,255,255,0.7); }

  .platter-name { top: 340px; font-family: "Archivo Narrow", "Arial Narrow", sans-serif; font-weight: 700; font-size: 60px; line-height: 62px; color: var(--green); letter-spacing: 1px; }
  .choice-script { top: 455px; font-family: "Great Vibes", cursive; font-size: 46px; color: var(--red); }
  .platter-desc { top: 525px; left: 40px; width: 720px; font-size: 27px; line-height: 38px; color: var(--ink); }
  .platter-price { top: 672px; font-weight: 900; font-size: 66px; color: var(--red); }

  .fish-title { top: 830px; left: 0; width: 720px; font-family: "Archivo Narrow", "Arial Narrow", sans-serif; font-weight: 700; font-size: 72px; line-height: 68px; color: var(--white); }
  .fridays-badge { position: absolute; left: 608px; top: 838px; width: 116px; height: 116px; border-radius: 50%; background: var(--green); border: 4px solid var(--white); display: flex; align-items: center; justify-content: center; text-align: center; font-weight: 900; font-size: 22px; line-height: 24px; color: var(--white); }
  .fish-desc { top: 990px; left: 30px; width: 740px; font-weight: 700; font-size: 26px; line-height: 36px; color: var(--yellow); }
  .fish-price { top: 1108px; font-weight: 900; font-size: 68px; color: var(--yellow); }
</style>
</head>
<body>
<main class="sign">
  <svg class="backdrop" width="800" height="1200" viewBox="0 0 800 1200" aria-hidden="true">
    <defs>
      <linearGradient id="greenBand" x1="0" y1="0" x2="0" y2="1">
        <stop offset="0" stop-color="#0f6a27"/>
        <stop offset="1" stop-color="#2a9b45"/>
      </linearGradient>
      <linearGradient id="redBand" x1="0" y1="0" x2="0" y2="1">
        <stop offset="0" stop-color="#e52a2f"/>
        <stop offset="1" stop-color="#a3141c"/>
      </linearGradient>
    </defs>
    <!-- top salad band -->
    <path d="M0 0 H800 V240 C620 270 520 320 400 310 C260 300 120 340 0 400 Z" fill="url(#greenBand)"/>
    <path d="M0 400 C120 340 260 300 400 310 C520 320 620 270 800 240 V252 C620 284 520 334 400 324 C260 314 120 352 0 412 Z" fill="var(--red)"/>
    <!-- bottom fish fry band -->
    <path d="M0 760 C200 800 360 760 520 740 C640 725 730 730 800 745 V1200 H0 Z" fill="url(#redBand)"/>
    <path d="M0 744 C200 784 360 744 520 724 C640 709 730 714 800 729 V739 C730 724 640 719 520 734 C360 754 200 794 0 754 Z" fill="var(--green)"/>
    <!-- flourish lines around script -->
    <path d="M150 484 C200 470 240 490 270 480" stroke="var(--ink)" stroke-width="2" fill="none"/>
    <path d="M530 480 C560 490 600 470 650 484" stroke="var(--ink)" stroke-width="2" fill="none"/>
  </svg>
  <svg style="position:absolute;left:640px;top:0" width="160" height="110" role="img" aria-label="Floral ornament"><rect width="160" height="110" fill="rgba(255,255,255,0.12)" rx="55"/></svg>
  <svg style="position:absolute;left:0;top:250px" width="130" height="120" role="img" aria-label="Floral ornament"><rect width="130" height="120" fill="rgba(255,255,255,0.12)" rx="60"/></svg>
  <svg style="position:absolute;left:374px;top:288px" width="52" height="52" role="img" aria-label="Tomato illustration"><circle cx="26" cy="26" r="24" fill="#d8262c"/></svg>

  <h1 class="block salads-title">Fresh Garden Salads</h1>
  <div class="price-row row-plain"><span class="label">Plain:</span><span class="small">Small: <b>$2.99</b></span><span class="large">Large: <b>$4.99</b></span></div>
  <div class="row-divider"></div>
  <div class="price-row row-specialty"><span class="label">Specialty:</span><span class="small">Small: <b>$4.99</b></span><span class="large">Large: <b>$7.99</b></span></div>

  <h2 class="block platter-name">ROCCO'S<br>GARBAGE PLATTER</h2>
  <p class="block choice-script">Your choice of</p>
  <p class="block platter-desc">2 Hamburgs, Cheeseburgs, Hot Dogs or Italian Sausages with Fries and Mac or Potato Salad. Top with Onions, Meat Hot Sauce, Ketchup or Mustard.</p>
  <p class="block platter-price">$9.99</p>

  <h2 class="block fish-title">HADDOCK<br>FISH FRY</h2>
  <div class="fridays-badge">FRIDAYS<br>ONLY</div>
  <p class="block fish-desc">Your choice of Beer Battered, Breaded or Broiled with Potato Wedges, Coleslaw, Lemon, Salt, Pepper, Butter, Ketchup and a roll.</p>
  <p class="block fish-price">$9.99</p>
</main>
</body>
</html>
```